Company providing Business Management Services needs modern business card

The business provides services like tender preparation, bank submissions, business health checks, financial and admin support. We want to portray 'Trust', 'Strength' and 'Support'.
2 styles of logo in various formats have been uploaded.
Looking for easy to understand, yet sophisticated and stand out from the crowd.

Target Market(s)

Small and Medium sized businesses

Industry/Entity Type

Business

Contact Information for Business Card

Name - Daniel Vesterby, Description - Manager, Phone - 0472 915 603, Email - danielvesterby@kpwholdingsgroup.example, Work description - Business Management Services.

Requirements
Must have
• Logo

```html
<!DOCTYPE html>
<html lang="en">
<head>
<meta charset="utf-8">
<title>KPW Holdings Group – Business Card</title>
<link rel="stylesheet" href="https://fonts.googleapis.com/css2?family=Exo+2:wght@300;400;600;700&display=swap">
<style>
  :root {
    --backdrop: #3a1416;
    --card: #e3e4e6;
    --card-edge: #cfd0d3;
    --ink: #47494d;
    --ink-soft: #5a5c60;
    --purple: #8e35a0;
    --blue: #2167bf;
    --green: #4cae3f;
    --orange: #f07d22;
    --band-text: #ffffff;
  }
  * { box-sizing: border-box; margin: 0; padding: 0; }
  html, body {
    width: 1200px;
    height: 900px;
    overflow: hidden;
    background: var(--backdrop);
    font-family: "Exo 2", sans-serif;
  }
  .business-card {
    position: absolute;
    left: 160px;
    top: 175px;
    width: 880px;
    height: 550px;
    border-radius: 30px;
    background: linear-gradient(160deg, #eeeff1 0%, var(--card) 55%, var(--card-edge) 100%);
    overflow: hidden;
    color: var(--ink);
  }
  .brand {
    position: absolute;
    top: 62px;
    left: 0;
    width: 100%;
    display: flex;
    justify-content: center;
    align-items: center;
    gap: 16px;
  }
  .brand-square {
    width: 54px;
    height: 54px;
    background: var(--ink);
  }
  .brand-name {
    font-size: 38px;
    font-weight: 600;
    letter-spacing: 1px;
    color: var(--ink);
  }
  .identity {
    position: absolute;
    top: 160px;
    left: 0;
    width: 100%;
    text-align: center;
  }
  .person-name {
    font-size: 60px;
    font-weight: 700;
    line-height: 1.05;
    color: var(--ink);
  }
  .person-role {
    font-size: 34px;
    font-weight: 300;
    letter-spacing: 1px;
    color: var(--ink-soft);
    margin-top: 2px;
  }
  .contact {
    position: absolute;
    top: 300px;
    left: 0;
    width: 100%;
    display: flex;
    flex-direction: column;
    align-items: center;
    gap: 22px;
    font-size: 25px;
    font-weight: 300;
    color: var(--ink-soft);
  }
  .contact-line {
    display: flex;
    align-items: center;
    gap: 14px;
  }
  .contact-icon { width: 26px; height: 26px; fill: var(--ink-soft); }
  .service-band {
    position: absolute;
    left: 0;
    bottom: 40px;
    width: 880px;
    height: 48px;
  }
  .service-band text {
    font-family: "Exo 2", sans-serif;
    font-size: 27px;
    font-weight: 300;
    fill: var(--band-text);
  }
</style>
</head>
<body>
  <article class="business-card">
    <header class="brand">
      <span class="brand-square"></span>
      <span class="brand-name">KPW HOLDINGS GROUP</span>
    </header>

    <section class="identity">
      <h1 class="person-name">Daniel Vesterby</h1>
      <p class="person-role">MANAGER</p>
    </section>

    <section class="contact">
      <p class="contact-line">
        <svg class="contact-icon" viewBox="0 0 24 24" aria-hidden="true">
          <path d="M6.6 10.8c1.4 2.8 3.8 5.1 6.6 6.6l2.2-2.2c.3-.3.7-.4 1-.2 1.1.4 2.3.6 3.6.6.6 0 1 .4 1 1V20c0 .6-.4 1-1 1C10.6 21 3 13.4 3 4c0-.6.4-1 1-1h3.5c.6 0 1 .4 1 1 0 1.3.2 2.5.6 3.6.1.3 0 .7-.2 1z"/>
        </svg>
        <span>0472 915 603</span>
      </p>
      <p class="contact-line">
        <svg class="contact-icon" viewBox="0 0 24 24" aria-hidden="true">
          <path d="M2 5h20v14H2z M4 7v.4l8 5.2 8-5.2V7z M4 9.8V17h16V9.8l-8 5.2z" fill-rule="evenodd"/>
        </svg>
        <span>danielvesterby@kpwholdingsgroup.example</span>
      </p>
    </section>

    <svg class="service-band" viewBox="0 0 880 48" aria-label="Business Management Services">
      <polygon points="0,0 150,0 135,48 0,48" fill="var(--purple)"/>
      <polygon points="150,0 350,0 335,48 135,48" fill="var(--blue)"/>
      <polygon points="350,0 650,0 635,48 335,48" fill="var(--green)"/>
      <polygon points="650,0 880,0 880,48 635,48" fill="var(--orange)"/>
      <text x="242" y="33" text-anchor="middle">Business</text>
      <text x="492" y="33" text-anchor="middle">Management</text>
      <text x="760" y="33" text-anchor="middle">Services</text>
    </svg>
  </article>
</body>
</html>
```